Create an awesome website for a medical clinic

This is a new website for a doctor's office. The site should be clean and modern, easy to navigate.

This is a wellness clinic, we want to help our clients have a healthy, active lifestyle. It should be friendly and inviting, and easy for them to call or schedule an appointment.

The site should be responsive and designed using the attached Bootstrap 3 PSD.

We will provide stock photos, until then please use stock photos from:

photoharvestbin.net or
lumapicturevault.net (preferred)

Some example sites of clean and modern designs that we like:

https://tarnelspine.example/
http://walkpastjoints.example/
http://feelingbrisker.example/

Also attached is a temporary logo you can use.
Updates

Reason: Thank you everyone for your great designs - we need a little more time so I'm extending the project.

Need extra days to review

Also, the colors in the new logo I just linked to are the final colors of the logo, so feel free to use any complimentary colors to it.

Hi everyone, The boss wants to change the layout of the site a little bit - here's the revised layout: https://www.filecrate.example/s/q8vn31kd2pxe74rt/memo%2011_29_2017.pdf?dl=0 And the graphic assets you can use are here: https://www.filecrate.example/s/q8vn31kd2pxe74rt/memo%2011_29_2017.pdf?dl=0 Feel free to change the background color of the "topbar", and change the icons of the "why people trust us" if you want, these are just temporary placeholders. Thanks for your patience and hard work!

Target Market(s)

People seeking medical treatment (wellness clinic)

Industry/Entity Type

Doctor

Number of Pages Required

1 page

Font styles to use
Sans Serif

Colors
0592cd
33a6d7
abd037
9bcb3c

Requirements
Must have
• The home page should have: a strong hero image/slideshow, clinic phone number should be prominent and at the top of the page (in the nav), a "what to expect" section (this is like a FAQs section - see attachment), and a strong call to action (a button to call or schedule an appointment).
• The what to expect section is useful so that prospective clients can determine if we're a good fit for them or not. It's a basic, first-step pre-qualification block of information.
• Social media icons which links to our social media profiles should be included.
Nice to have
• - Link to 3 most recent blog entries
• - Testimonials
• - How a multilevel nav menu looks.

```html
<!DOCTYPE html>
<html lang="en">
<head>
<meta charset="utf-8">
<title>Medical Clinic</title>
<link rel="stylesheet" href="https://fonts.googleapis.com/css2?family=Lato:wght@300;400;700&family=Open+Sans:wght@300;400;600;700&display=swap">
<style>
:root{
  --blue:#0592cd;
  --blue-light:#33a6d7;
  --green:#abd037;
  --green-dark:#9bcb3c;
  --text:#222;
  --muted:#777;
  --white:#fff;
  --input:#33a6d7;
}
*{margin:0;padding:0;box-sizing:border-box}
html,body{width:1200px;height:1088px;overflow:hidden;background:var(--white)}
body{position:relative;font-family:"Open Sans",sans-serif;color:var(--text)}
.abs{position:absolute}

/* doctors */
.doctor-card{position:absolute;top:-10px;width:200px;height:272px;border:2px solid var(--green);border-top:none;background:var(--white);text-align:center}
.doctor-photo{height:64px;background:linear-gradient(180deg,#e9eef2,#c9d5de)}
.doctor-name{margin-top:12px;font-family:"Lato",sans-serif;font-weight:700;font-size:14px;color:#333}
.doctor-bio{margin:11px 10px 0;font-family:"Lato",sans-serif;font-weight:300;font-size:11.5px;line-height:18.4px;color:var(--muted)}
.btn-read{display:inline-block;margin-top:19px;width:105px;height:37px;line-height:37px;border-radius:3px;background:var(--green);color:var(--white);font-family:"Lato",sans-serif;font-weight:300;font-size:12px}

/* info */
.section-title{position:absolute;top:356px;font-size:22px;font-weight:300;color:var(--blue-light)}
.section-title b{font-weight:700;color:var(--blue)}
.divider{position:absolute;left:600px;top:366px;width:1px;height:236px;background:#ccc}
.avatar{position:absolute;left:310px;top:408px;width:76px;height:76px;border-radius:50%;background:linear-gradient(180deg,#c9c2bb,#6a5a50)}
.quote{position:absolute;left:188px;top:499px;width:320px;text-align:center;font-size:11.3px;line-height:13.5px;color:#222}
.quote-author{position:absolute;left:188px;top:562px;width:320px;text-align:center;font-size:11.5px;color:var(--blue)}
.dots{position:absolute;display:flex;gap:6px}
.dots span{width:7px;height:7px;border-radius:50%;background:#9a9aa8}
.dots span:first-child{background:#555}
.faq-q{position:absolute;left:674px;top:402px;width:330px;font-size:18px;line-height:26px;color:var(--blue)}
.faq-a{position:absolute;left:674px;top:470px;width:330px;font-size:11.3px;line-height:15.2px;color:#222}

/* footer */
.site-footer{position:absolute;left:0;top:722px;width:1200px;height:366px;background:var(--blue);color:var(--white)}
.footer-heading{position:absolute;font-size:17px;font-weight:600}
.footer-links{position:absolute;list-style:none;font-size:11.5px}
.footer-links li{height:24.8px}
.footer-links .active{color:#d9ef7a}
.newsletter-intro{position:absolute;left:426px;top:64px;font-size:11.5px;line-height:13px}
.field{position:absolute;left:425px;width:168px;height:26px;border-radius:3px;background:var(--input);color:#a9d4ec;font-size:9px;padding:7px 10px}
.btn-subscribe{position:absolute;left:425px;top:183px;width:72px;height:26px;border-radius:3px;background:var(--green);font-size:11.5px;line-height:26px;text-align:center}
.tweet{position:absolute;left:640px;width:190px;font-size:9px;line-height:11.3px}
.tweet em{display:block;font-style:normal;color:#d9ef7a}
.contact-row{position:absolute;left:890px;font-size:11.5px}
.contact-icon{position:absolute;left:857px}
.footer-rule{position:absolute;left:173px;top:318px;width:861px;height:1px;background:#5fb6dd}
.copyright{position:absolute;left:186px;top:335px;font-size:11.5px}
.social{position:absolute;left:870px;top:339px;display:flex;gap:10px}
.social span{width:15px;height:15px;border-radius:50%;background:var(--white)}
</style>
</head>
<body>

<section class="doctors">
  <article class="doctor-card" style="left:174px">
    <div class="doctor-photo" role="img" aria-label="Portrait photo of a doctor in white coat"></div>
    <h3 class="doctor-name">Dr.Elwin Marchetti</h3>
    <p class="doctor-bio">This text represents a brief introduction of doctor and this text will be displayed on homepage and all the places where multiple doctors are listed.</p>
    <a class="btn-read">Read more</a>
  </article>
  <article class="doctor-card" style="left:392px">
    <div class="doctor-photo" role="img" aria-label="Portrait photo of a doctor holding a clipboard"></div>
    <h3 class="doctor-name">Dr.Conrad Vell</h3>
    <p class="doctor-bio">This text represents a brief introduction of doctor and this text will be displayed on homepage and all the places where multiple doctors are listed.</p>
    <a class="btn-read">Read more</a>
  </article>
  <article class="doctor-card" style="left:612px">
    <div class="doctor-photo" role="img" aria-label="Portrait photo of a doctor in scrubs"></div>
    <h3 class="doctor-name">Dr.Marisa Quenby</h3>
    <p class="doctor-bio">This text represents a brief introduction of doctor and this text will be displayed on homepage and all the places where multiple doctors are listed.</p>
    <a class="btn-read">Read more</a>
  </article>
  <article class="doctor-card" style="left:830px">
    <div class="doctor-photo" role="img" aria-label="Portrait photo of a doctor in white coat"></div>
    <h3 class="doctor-name">Dr.Elwin Marchetti</h3>
    <p class="doctor-bio">This text represents a brief introduction of doctor and this text will be displayed on homepage and all the places where multiple doctors are listed.</p>
    <a class="btn-read">Read more</a>
  </article>
</section>

<section class="testimonial">
  <h2 class="section-title" style="left:244px">Patient <b>Testimonial</b></h2>
  <div class="avatar" role="img" aria-label="Portrait photo of the patient"></div>
  <p class="quote">A big thank you to you and all your staff for all that you did to help us achieve our dream of having a baby… We can’t wait to come back for our blastocysts to give our baby some brothers or sisters!</p>
  <p class="quote-author">Mr. Ravina Oshel, Kestrelford</p>
  <div class="dots" style="left:333px;top:593px"><span></span><span></span><span></span></div>
</section>

<div class="divider"></div>

<section class="faq">
  <h2 class="section-title" style="left:674px">Patient <b>FAQ</b></h2>
  <h3 class="faq-q">How to become a patient at LMCH Fertility Clinic</h3>
  <p class="faq-a">he decision to seek fertility treatments is never an easy one. There are so many things to consider and a couple having trouble conceiving or maintaining a pregnancy should really weigh their options before pursuing the next step. However, once you know that fertility treatment is the right choice for you, it’s time to fi</p>
  <div class="dots" style="left:785px;top:601px"><span></span><span></span><span></span></div>
</section>

<footer class="site-footer">
  <h4 class="footer-heading" style="left:178px;top:20px">Important Links</h4>
  <ul class="footer-links" style="left:184px;top:69px">
    <li class="active">Home</li><li>About Us</li><li>Services</li><li>Why Us</li><li>Specialities</li><li>Events</li><li>Doctors</li>
  </ul>
  <ul class="footer-links" style="left:282px;top:71px">
    <li>Departments</li><li>Blog</li><li>Meet The Team</li><li>Shortcodes</li><li>Contact Us</li>
  </ul>

  <h4 class="footer-heading" style="left:434px;top:20px">New Letter</h4>
  <p class="newsletter-intro">Sign up with your name and email<br>to get updates fresh updates.</p>
  <div class="field" style="top:103px">Your Name</div>
  <div class="field" style="top:143px">Your Email Address</div>
  <div class="btn-subscribe">Subscribe</div>

  <h4 class="footer-heading" style="left:642px;top:20px">Latest Tweets</h4>
  <p class="tweet" style="top:63px">We've released new version (v3.8) of our #Timetable #Responsive #Schedule #WP Plugin. Please check at #ScriptBazaar lnk.example/q7Rv2a<em>10 days ago</em></p>
  <p class="tweet" style="top:138px">We've released new version (v3.8) of our #Timetable #Responsive #Schedule #WP Plugin. Please check at #ScriptBazaar lnk.example/q7Rv2a<em>10 days ago</em></p>
  <p class="tweet" style="top:218px;left:642px">We've released new version (v3.8) of our #Timetable #Responsive #Schedule #WP Plugin. Please check at #ScriptBazaar lnk.example/q7Rv2a<em>10 days ago</em></p>

  <h4 class="footer-heading" style="left:884px;top:18px">Get in Touch</h4>
  <svg class="contact-icon" style="top:64px" width="24" height="24" viewBox="0 0 24 24"><rect x="1" y="1" width="22" height="22" rx="4" fill="var(--green)"/><path d="M8 6c1 0 2 2 2 3s-1 1-1 2 2 3 3 3 1-1 2-1 3 1 3 2-1 2-2 2C10 17 7 12 7 8c0-1 0-2 1-2z" fill="var(--white)"/></svg>
  <div class="contact-row" style="top:67px">(+09) 0555 010 2987</div>
  <svg class="contact-icon" style="top:98px" width="24" height="18" viewBox="0 0 24 18"><rect x="0" y="0" width="24" height="18" rx="2" fill="var(--green)"/><path d="M1 2l11 8 11-8" stroke="var(--blue)" stroke-width="2" fill="none"/></svg>
  <div class="contact-row" style="top:99px">help@mendwell.example</div>
  <svg class="contact-icon" style="top:127px" width="24" height="24" viewBox="0 0 24 24"><circle cx="12" cy="12" r="10.5" stroke="var(--green)" stroke-width="2.5" fill="none"/><path d="M12 6v6h-4" stroke="var(--green)" stroke-width="2" fill="none"/></svg>
  <div class="contact-row" style="top:131px">Mon - Sat 9:00am - 6:00 pm</div>
  <svg class="contact-icon" style="top:159px" width="22" height="22" viewBox="0 0 22 22"><rect x="1.5" y="1.5" width="19" height="19" rx="3" stroke="var(--green)" stroke-width="2.5" fill="none"/><path d="M7 5v12M15 5v12M7 11h8" stroke="var(--green)" stroke-width="3"/></svg>
  <div class="contact-row" style="top:163px">Mendwell Home Care, LLC</div>

  <div class="footer-rule"></div>
  <p class="copyright">© Copyright 2017. All Rights Reserved by Verdant Medical Clinic</p>
  <div class="social" aria-label="Social media profiles">
    <span></span><span></span><span></span><span></span><span></span><span></span><span></span>
  </div>
</footer>

</body>
</html>
```